App for Lawyers & Accountants needs 'Professional' Styling

We want to style our app to convey a 'Professional' appearance. It's used by Lawyers, Accountants, Doctors etc. who take their work very seriously.

We currently trying to follow corvane layout guidelines, but we find our app looks very bland. I've uploaded a screenshot of our current app, and two mock-ups of more stylized versions, but we're not happy with those mock-ups.

We'd like to see alternate designs for those two mock-ups, that look much more professional.

The specific elements we'd like to improve/focus on are:
* Colour of the top and left nav bars
* Appearance of the left nav, size, icons spacing
* Appearance of the buttons on the top right, so the user knows they are buttons they can press
* Spacing of the dashboard, background colour and spacing, colour/layout of the 'overdue' and 'todo' accordion headings in the 'my tasks' section.
* List view background grey, to be consistent with dashboard, but unobtrusive
* List view tabs to be obvious as tabs, but 'saved searches', filters and the export icon to still be associated with the data displayed, but it should be obvious to the user that those are different buttons, not just more tabs. (I.e. the filters button opens a panel below it that allows the user to filter the data in the list.)
* General appearance of the popup menu when you push the 'add' button on the top right

However, despite those specifics I'm sure it's all the subtle elements of the design that make a big difference.

Our brand colour is 1D4F91, and we use A20067 as a secondary colour in print media, (although it doesn't seem to work to well within the app.) Our brand font is signika. We'd like the designs to be based on those colours & font.

Professional people, Lawyers, Accountants, Doctors etc.

Sans Serif
• Signika

0255a3

• The most 'Professional' experience/quality possible. Think the quality & brand image of brindlewave desk, but taken to a higher level.
• An example/mock-up of the dashboard, list view and 'add' item popup menu
• Display the dashboard cards with the same information as our mock-ups - the information there is important and we don't have any extra cards to add (in the near term)
• Various colour combinations for the top and left nav bars, based on our primary blue brand colour, and perhaps some shade of dark grey.

```html
<!DOCTYPE html>
<html lang="en">
<head>
<meta charset="utf-8">
<title>Dashboard</title>
<link rel="stylesheet" href="https://fonts.googleapis.com/css2?family=Signika:wght@300;400;500;600&display=swap">
<style>
:root{
  --stage:#262a3b;
  --brand:#1d4f91;
  --accent:#a20067;
  --ink:#2a2c38;
  --ink-soft:#5c5f6b;
  --muted:#9a9ca6;
  --canvas:#f4f5f8;
  --card:#ffffff;
  --line:#e4e6ec;
  --chart-bg:#e9ecf2;
  --wave:#c9d0de;
  --legend-blue:#a9b9d6;
  --word:#1f5fb4;
  --sheet:#217346;
  --slides:#d24726;
}
*{box-sizing:border-box;margin:0;padding:0}
html,body{width:1200px;height:920px;overflow:hidden}
body{background:var(--stage);font-family:"Signika",sans-serif;font-weight:300;color:var(--ink);position:relative}
.app{position:absolute;left:19px;top:133px;width:1162px;height:653px;background:var(--card);border-radius:16px;overflow:hidden}
.abs{position:absolute}

/* sidebar */
.sidebar{left:0;top:0;width:207px;height:100%;background:var(--card)}
.menu-icon{left:15px;top:25px}
.app-name{left:47px;top:20px;font-size:16px;font-weight:400;color:var(--brand);letter-spacing:.3px}
.search{left:12px;top:61px;width:181px;height:29px;background:var(--canvas);border-radius:3px;font-size:12px;color:var(--muted);padding:7px 11px}
.search svg{position:absolute;right:10px;top:9px}
.avatar{left:37px;top:115px;width:48px;height:48px;border-radius:50%;background:radial-gradient(circle at 50% 40%,#d9b8a4,#8a4e40 70%)}
.new-btn{left:133px;top:115px;width:48px;height:48px;border-radius:50%;background:linear-gradient(160deg,var(--brand),var(--accent));display:flex;align-items:center;justify-content:center}
.user-label,.new-label{top:172px;font-size:10px;font-weight:400;width:80px;text-align:center;color:var(--ink)}
.user-label{left:21px}.new-label{left:117px}
.nav-item{left:0;width:207px;height:24px;display:flex;align-items:center;font-size:11.5px;color:var(--ink-soft)}
.nav-item svg{position:absolute;left:21px}
.nav-item span{position:absolute;left:56px}
.nav-item.active span{color:var(--brand);font-weight:500}
.nav-item.active::before{content:"";position:absolute;left:0;top:0;width:3px;height:24px;background:var(--brand)}
.badge{position:absolute;left:178px;width:16px;height:16px;border-radius:50%;background:var(--accent);color:#fff;font-size:8px;font-weight:400;display:flex;align-items:center;justify-content:center}

/* main */
.main{left:207px;top:0;width:658px;height:100%;background:var(--canvas)}
.page-title{left:27px;top:19px;font-size:18px;color:var(--ink);font-weight:400}
.card{background:var(--card);box-shadow:0 1px 3px rgba(30,40,70,.08);overflow:hidden}
.card-title{position:absolute;left:18px;font-size:12.5px;font-weight:400;color:var(--ink)}

.matters{left:28px;top:66px;width:290px;height:569px}
.matters .card-title{top:20px}
.matter{position:absolute;left:0;width:290px;height:44px}
.matter .dot{position:absolute;left:12px;top:2px;width:29px;height:29px;border-radius:50%;background:var(--canvas);display:flex;align-items:center;justify-content:center}
.matter p{position:absolute;left:54px;top:0;width:200px;font-size:11.5px;line-height:16px;color:var(--ink)}
.matter time{position:absolute;right:12px;top:1px;font-size:9.5px;color:var(--muted)}

.time-card{left:342px;top:66px;width:291px;height:291px}
.time-card .card-title{top:20px}
.period{position:absolute;top:55px;width:90px;text-align:center;transform:translateX(-45px)}
.period small{display:block;font-size:7.5px;color:var(--ink-soft);letter-spacing:.4px}
.period b{display:block;font-size:15px;font-weight:300;margin-top:5px;color:var(--ink)}
.period.current small,.period.current b{color:var(--accent)}
.period-line{left:115px;top:90px;width:61px;height:2px;background:var(--accent)}
.chart{left:0;top:96px}
.legend{top:265px;font-size:9.5px;color:var(--ink);display:flex;align-items:center;gap:10px}
.legend i{width:12px;height:12px;border-radius:50%;display:inline-block}

.docs{left:342px;top:381px;width:291px;height:254px}
.docs .card-title{top:20px}
.doc{position:absolute;left:0;width:291px;height:18px;font-size:9.5px;color:var(--ink)}
.doc i{position:absolute;left:13px;top:2px;width:14px;height:14px;border-radius:2px}
.doc span{position:absolute;left:41px;top:3px}
.doc time{position:absolute;right:12px;top:3px;color:var(--muted)}

/* tasks */
.tasks{left:865px;top:0;width:297px;height:100%;background:var(--card);border-left:1px solid var(--line)}
.tasks-title{left:18px;top:19px;font-size:13px;font-weight:400}
.tab{top:55px;font-size:9.5px;font-weight:400;width:100px;text-align:center;color:var(--ink)}
.tab.overdue{left:29px}
.tab.todo{left:174px;color:var(--accent);font-weight:500}
.tab-line{left:182px;top:77px;width:84px;height:2px;background:var(--accent)}
.task{position:absolute;left:0;width:297px;height:40px}
.task .check{position:absolute;left:17px;top:1px;width:13px;height:13px;border-radius:50%;border:1.3px solid var(--ink-soft)}
.task .check.done{border:none;background:var(--accent);display:flex;align-items:center;justify-content:center}
.task h4{position:absolute;left:41px;top:0;font-size:11.5px;font-weight:400;color:var(--ink)}
.task time{position:absolute;right:12px;top:1px;font-size:9px;color:var(--muted)}
.task p{position:absolute;left:41px;top:17px;font-size:9.5px;color:var(--ink-soft);display:flex;align-items:center;gap:6px}
.task p svg{flex:none}
</style>
</head>
<body>
<div class="app">

  <aside class="abs sidebar">
    <svg class="abs menu-icon" width="16" height="12" viewBox="0 0 16 12"><path d="M0 1h16M0 6h16M0 11h16" stroke="#444" stroke-width="1.5"/></svg>
    <div class="abs app-name">AppName</div>
    <div class="abs search">Search everything
      <svg width="10" height="10" viewBox="0 0 10 10"><circle cx="4" cy="4" r="3.2" fill="none" stroke="#777" stroke-width="1.2"/><path d="M6.4 6.4L9.5 9.5" stroke="#777" stroke-width="1.2"/></svg>
    </div>
    <div class="abs avatar" role="img" aria-label="User profile photo"></div>
    <div class="abs new-btn"><svg width="14" height="14" viewBox="0 0 14 14"><path d="M7 1v12M1 7h12" stroke="#fff" stroke-width="2"/></svg></div>
    <div class="abs user-label">Reid T.</div>
    <div class="abs new-label">NEW</div>

    <nav>
      <div class="abs nav-item active" style="top:218px">
        <svg width="16" height="16" viewBox="0 0 16 16"><circle cx="8" cy="8" r="7.5" fill="var(--brand)"/><path d="M8 8L11.5 4.5" stroke="#fff" stroke-width="1.5"/><circle cx="8" cy="8" r="1.5" fill="#fff"/></svg>
        <span>Dashboard</span></div>
      <div class="abs nav-item" style="top:254px">
        <svg width="16" height="14" viewBox="0 0 16 14"><rect x="5.5" y="0.5" width="5" height="3" fill="none" stroke="#666"/><rect x="0" y="3" width="16" height="11" rx="1" fill="#666"/></svg>
        <span>My Matters</span></div>
      <div class="abs nav-item" style="top:291px">
        <svg width="16" height="16" viewBox="0 0 16 16"><circle cx="8" cy="4.5" r="4" fill="#666"/><path d="M1 16c0-5 3-7 7-7s7 2 7 7z" fill="#666"/></svg>
        <span>Account</span></div>
      <div class="abs nav-item" style="top:327px">
        <svg width="16" height="16" viewBox="0 0 16 16"><path d="M15 1L1 7l5 2 2 6z" fill="#666"/></svg>
        <span>My Tasks</span><b class="badge">24</b></div>
      <div class="abs nav-item" style="top:364px">
        <svg width="16" height="16" viewBox="0 0 16 16"><path d="M11 4l-6 6a1.5 1.5 0 0 0 2 2l7-7a3 3 0 0 0-4-4L3 8a4.5 4.5 0 0 0 6 6l5-5" fill="none" stroke="#666" stroke-width="1.4"/></svg>
        <span>Documents</span></div>
      <div class="abs nav-item" style="top:401px">
        <svg width="16" height="16" viewBox="0 0 16 16"><path d="M2.5 8a6 6 0 1 0 1.8-4.3" fill="none" stroke="#666" stroke-width="1.4"/><path d="M1 2v4h4" fill="none" stroke="#666" stroke-width="1.4"/><path d="M8.5 4.5V8.5l2.5 1.5" fill="none" stroke="#666" stroke-width="1.4"/></svg>
        <span>Time Records</span></div>
      <div class="abs nav-item" style="top:617px">
        <svg width="16" height="16" viewBox="0 0 16 16"><circle cx="8" cy="8" r="5.5" fill="none" stroke="#666" stroke-width="3" stroke-dasharray="3 1.3"/><circle cx="8" cy="8" r="2" fill="#666"/></svg>
        <span style="color:var(--ink)">Settings</span></div>
    </nav>
  </aside>

  <main class="abs main">
    <h1 class="abs page-title">Dashboard</h1>

    <section class="abs card matters">
      <h2 class="card-title">My Recent Matters</h2>
      <div class="matter" style="top:57px"><div class="dot"><svg width="13" height="11" viewBox="0 0 13 11"><rect x="4" y="0.5" width="5" height="2.5" fill="none" stroke="var(--accent)"/><rect y="2.5" width="13" height="8.5" rx="1" fill="var(--accent)"/></svg></div><p>1157 Abbott v. Director of Public Persecutions concerning motor vehicle</p><time>2h</time></div>
      <div class="matter" style="top:111px"><div class="dot"><svg width="13" height="11" viewBox="0 0 13 11"><rect x="4" y="0.5" width="5" height="2.5" fill="none" stroke="var(--accent)"/><rect y="2.5" width="13" height="8.5" rx="1" fill="var(--accent)"/></svg></div><p>The generated Lorem Ipsum is therefore always free from repetition</p><time>5h</time></div>
      <div class="matter" style="top:166px"><div class="dot"><svg width="13" height="11" viewBox="0 0 13 11"><rect x="4" y="0.5" width="5" height="2.5" fill="none" stroke="var(--accent)"/><rect y="2.5" width="13" height="8.5" rx="1" fill="var(--accent)"/></svg></div><p>1024 Lorem Ipsum is not simply<br>random text.</p><time>12h</time></div>
      <div class="matter" style="top:220px"><div class="dot"><svg width="13" height="11" viewBox="0 0 13 11"><rect x="4" y="0.5" width="5" height="2.5" fill="none" stroke="var(--accent)"/><rect y="2.5" width="13" height="8.5" rx="1" fill="var(--accent)"/></svg></div><p>Roland Mercer, a Latin professor at Halden-Sable College in Virginia</p><time>20h</time></div>
      <div class="matter" style="top:275px"><div class="dot"><svg width="13" height="11" viewBox="0 0 13 11"><rect x="4" y="0.5" width="5" height="2.5" fill="none" stroke="var(--accent)"/><rect y="2.5" width="13" height="8.5" rx="1" fill="var(--accent)"/></svg></div><p>The standard chunk of Lorem Ipsum<br>used since the 1500s</p><time>1d</time></div>
      <div class="matter" style="top:329px"><div class="dot"><svg width="13" height="11" viewBox="0 0 13 11"><rect x="4" y="0.5" width="5" height="2.5" fill="none" stroke="var(--accent)"/><rect y="2.5" width="13" height="8.5" rx="1" fill="var(--accent)"/></svg></div><p>1157 Abbott v. Director of Public Persecutions concerning motor vehi-</p><time>2d</time></div>
      <div class="matter" style="top:383px"><div class="dot"><svg width="13" height="11" viewBox="0 0 13 11"><rect x="4" y="0.5" width="5" height="2.5" fill="none" stroke="var(--accent)"/><rect y="2.5" width="13" height="8.5" rx="1" fill="var(--accent)"/></svg></div><p>The generated Lorem Ipsum is there-<br>fore always free from repetition</p><time>5d</time></div>
      <div class="matter" style="top:438px"><div class="dot"><svg width="13" height="11" viewBox="0 0 13 11"><rect x="4" y="0.5" width="5" height="2.5" fill="none" stroke="var(--accent)"/><rect y="2.5" width="13" height="8.5" rx="1" fill="var(--accent)"/></svg></div><p>1024 Lorem Ipsum is not simply<br>random text.</p><time>7d</time></div>
      <div class="matter" style="top:492px"><div class="dot"><svg width="13" height="11" viewBox="0 0 13 11"><rect x="4" y="0.5" width="5" height="2.5" fill="none" stroke="var(--accent)"/><rect y="2.5" width="13" height="8.5" rx="1" fill="var(--accent)"/></svg></div><p>Roland Mercer, a Latin professor at Halden-Sable College in Virgin-</p><time>1w</time></div>
      <div class="matter" style="top:547px"><div class="dot"><svg width="13" height="11" viewBox="0 0 13 11"><rect x="4" y="0.5" width="5" height="2.5" fill="none" stroke="var(--accent)"/><rect y="2.5" width="13" height="8.5" rx="1" fill="var(--accent)"/></svg></div><p>The standard chunk of Lorem Ipsum<br>used since the 1500s</p><time>1w</time></div>
    </section>

    <section class="abs card time-card">
      <h2 class="card-title">My Time Records</h2>
      <div class="period" style="left:49px"><small>TODAY</small><b>5h 2m</b></div>
      <div class="period current" style="left:146px"><small>THIS WEEK</small><b>24h 7m</b></div>
      <div class="period" style="left:243px"><small>THIS MONTH</small><b>56h 34m</b></div>
      <div class="abs period-line"></div>
      <svg class="abs chart" width="291" height="170" viewBox="0 96 291 170" font-family="Signika, sans-serif">
        <rect x="0" y="172" width="291" height="82" fill="var(--chart-bg)"/>
        <path d="M0 184 C30 186 55 190 90 175 C130 158 150 147 180 147 C220 147 250 162 291 168 L291 254 L0 254 Z" fill="var(--wave)" opacity=".7"/>
        <path d="M0 209 C40 200 70 158 114 158 C150 158 170 194 207 194 C235 194 250 172 269 164 C278 161 285 159 291 158" fill="none" stroke="var(--accent)" stroke-width="1.8"/>
        <circle cx="269" cy="164" r="5" fill="#fff" stroke="var(--accent)" stroke-width="1.5"/>
        <g font-size="9" fill="#333" font-weight="300">
          <text x="12" y="109">10h</text><text x="12" y="133">8h</text><text x="12" y="157">6h</text><text x="12" y="181">4h</text><text x="12" y="205">2h</text>
        </g>
        <g font-size="6.5" fill="var(--brand)" text-anchor="middle">
          <text x="46" y="224">S</text><text x="83" y="224">M</text><text x="120" y="224">T</text><text x="158" y="224">W</text><text x="194" y="224">T</text><text x="232" y="224">F</text><text x="269" y="224">S</text>
        </g>
        <g font-size="9" fill="#333" text-anchor="middle">
          <text x="46" y="241">6</text><text x="83" y="241">7</text><text x="120" y="241">8</text><text x="158" y="241">9</text><text x="194" y="241">10</text><text x="232" y="241">11</text><text x="269" y="241">12</text>
        </g>
      </svg>
      <div class="abs legend" style="left:46px"><i style="background:var(--legend-blue)"></i>Last Week</div>
      <div class="abs legend" style="left:180px"><i style="background:var(--accent)"></i>Last Week</div>
    </section>

    <section class="abs card docs">
      <h2 class="card-title">My Recent Documents</h2>
      <div class="doc" style="top:59px"><i style="background:var(--word)"></i><span>Court Doc101</span><time>1h</time></div>
      <div class="doc" style="top:96px"><i style="background:var(--sheet)"></i><span>Settlement Figures_Cj-Lowell</span><time>4h</time></div>
      <div class="doc" style="top:132px"><i style="background:var(--slides)"></i><span>Vanguard 2018 Presentation</span><time>9h</time></div>
      <div class="doc" style="top:169px"><i style="background:var(--word)"></i><span>For Task XYZ000</span><time>12h</time></div>
      <div class="doc" style="top:205px"><i style="background:var(--sheet)"></i><span>Settlement Figures_Toby-Marsh</span><time>1d</time></div>
    </section>
  </main>

  <aside class="abs tasks">
    <h2 class="abs tasks-title">My Tasks</h2>
    <div class="abs tab overdue">OVERDUE (4)</div>
    <div class="abs tab todo">TO DO (20)</div>
    <div class="abs tab-line"></div>

    <div class="task" style="top:103px"><span class="check done"><svg width="8" height="6" viewBox="0 0 8 6"><path d="M1 3l2 2 4-4" fill="none" stroke="#fff" stroke-width="1.4"/></svg></span><h4>Finalise Court Documents</h4><time>Today</time><p><svg width="10" height="8" viewBox="0 0 10 8"><rect y="2" width="10" height="6" fill="#888"/><rect x="3" y="0.5" width="4" height="2" fill="none" stroke="#888"/></svg>1157 Ecerich v. The State of...</p></div>
    <div class="task" style="top:151px"><span class="check"></span><h4>Task #2</h4><time>Tomorrow</time><p><svg width="10" height="8" viewBox="0 0 10 8"><rect y="2" width="10" height="6" fill="#888"/><rect x="3" y="0.5" width="4" height="2" fill="none" stroke="#888"/></svg>Nolan Crane</p></div>
    <div class="task" style="top:200px"><span class="check"></span><h4>Finalise Court Settlement Figures</h4><time>15 May 2018</time><p><svg width="10" height="8" viewBox="0 0 10 8"><rect y="2" width="10" height="6" fill="#888"/><rect x="3" y="0.5" width="4" height="2" fill="none" stroke="#888"/></svg>1302 Vista Alameda v. The State of...</p></div>
    <div class="task" style="top:248px"><span class="check"></span><h4>This is my 4th task</h4><time>18 May 2018</time><p><svg width="10" height="8" viewBox="0 0 10 8"><rect y="2" width="10" height="6" fill="#888"/><rect x="3" y="0.5" width="4" height="2" fill="none" stroke="#888"/></svg>Short meeting with Toby Marsh</p></div>
    <div class="task" style="top:297px"><span class="check"></span><h4>No. 5 task</h4><time>22 May 2018</time><p><svg width="10" height="8" viewBox="0 0 10 8"><rect y="2" width="10" height="6" fill="#888"/><rect x="3" y="0.5" width="4" height="2" fill="none" stroke="#888"/></svg>Report to Vanguard HQ</p></div>
    <div class="task" style="top:345px"><span class="check"></span><h4>Finalise Court Documents</h4><time>26 May 2018</time><p><svg width="10" height="8" viewBox="0 0 10 8"><rect y="2" width="10" height="6" fill="#888"/><rect x="3" y="0.5" width="4" height="2" fill="none" stroke="#888"/></svg>1157 Ecerich v. The State of...</p></div>
    <div class="task" style="top:394px"><span class="check"></span><h4>Task #7</h4><time>27 May 2018</time><p><svg width="10" height="8" viewBox="0 0 10 8"><rect y="2" width="10" height="6" fill="#888"/><rect x="3" y="0.5" width="4" height="2" fill="none" stroke="#888"/></svg>Nolan Crane</p></div>
    <div class="task" style="top:442px"><span class="check"></span><h4>Finalise Court Settlement Figures</h4><time>1 Jun 2018</time><p><svg width="10" height="8" viewBox="0 0 10 8"><rect y="2" width="10" height="6" fill="#888"/><rect x="3" y="0.5" width="4" height="2" fill="none" stroke="#888"/></svg>1302 Vista Alameda v. The State of...</p></div>
    <div class="task" style="top:491px"><span class="check"></span><h4>This is my 9th task</h4><time>16 Jun 2018</time><p><svg width="10" height="8" viewBox="0 0 10 8"><rect y="2" width="10" height="6" fill="#888"/><rect x="3" y="0.5" width="4" height="2" fill="none" stroke="#888"/></svg>Short meeting with Toby Marsh</p></div>
    <div class="task" style="top:539px"><span class="check"></span><h4>No. 10 task</h4><time>4 Jul 2018</time><p><svg width="10" height="8" viewBox="0 0 10 8"><rect y="2" width="10" height="6" fill="#888"/><rect x="3" y="0.5" width="4" height="2" fill="none" stroke="#888"/></svg>Report to Vanguard HQ</p></div>
  </aside>

</div>
</body>
</html>
```